Attractive door board for entrance beautysalon

Make an attractive design for a board that can be glued on the front door of a beauty salon. The salon location has no window in the front so I need something catchy and attractive. The door board contains a list of the services and the website: www.velmora.be, and the text "Enkel op afspraak, bel 0486319542"

Target Market(s)

woman between 16 and 99 years old

Industry/Entity Type

Beauty Salon

Font styles to use
Sans Serif

Requirements
Must have
• A very nice, attractive but sober design.
• It must have a classy Marvaux, Quen, ... chique design.
• The logo must be on it (in attachment)
• There must be the following list in it:
• Gelaatsverzorging
• Wimperverlenging
• Wimperlifting
• Suikerontharing
• Permanente Make Up
• Airbrush Tanning
• Manicure - Pedicure - Tovira
• and then the website www.velmora.be, and the text "Enkel op afspraak, bel 0486319542"
Nice to have
• a catchy design,
• max. width can be 75 cm and max height 180 cm as it is a design for a board that will be glued on a door.
Should not have
• orchid flowers, buddha look a likes

```html
<!DOCTYPE html>
<html lang="nl">
<head>
<meta charset="utf-8">
<title>Velmora – deurbord</title>
<link rel="stylesheet" href="https://fonts.googleapis.com/css2?family=Questrial&display=swap">
<style>
  :root {
    --ink: #ffffff;
    --night: #0c0c0c;
    --silver-light: #f6f6f6;
    --silver-mid: #c4c4c4;
    --silver-dark: #707070;
  }
  * { margin: 0; padding: 0; box-sizing: border-box; }
  html, body {
    width: 1200px;
    height: 2877px;
    overflow: hidden;
    background: var(--night);
  }
  .door-board {
    position: relative;
    width: 1200px;
    height: 2877px;
    overflow: hidden;
    font-family: "Questrial", "Century Gothic", sans-serif;
    color: var(--ink);
    background: var(--night);
  }
  .backdrop {
    position: absolute;
    inset: 0;
    width: 1200px;
    height: 2877px;
  }
  .brand {
    position: absolute;
    top: 510px;
    left: 320px;
    width: 762px;
    text-align: center;
    font-weight: 400;
    font-size: 62px;
    letter-spacing: 0.62em;
    padding-left: 0.62em;
    line-height: 1;
  }
  .services {
    position: absolute;
    top: 1546px;
    left: 82px;
    list-style: none;
  }
  .services li {
    font-size: 60px;
    line-height: 1;
    height: 130px;
    display: flex;
    align-items: flex-start;
  }
  .services li::before {
    content: "";
    width: 16px;
    height: 16px;
    border-radius: 50%;
    background: var(--ink);
    margin: 24px 34px 0 0;
    flex: none;
  }
  .contact {
    position: absolute;
    top: 2515px;
    left: 130px;
  }
  .contact .web {
    font-size: 74px;
    line-height: 1;
    margin-bottom: 30px;
  }
  .contact .call {
    font-size: 56px;
    line-height: 1.36;
  }
</style>
</head>
<body>
<main class="door-board">
  <svg class="backdrop" viewBox="0 0 1200 2877">
    <defs>
      <radialGradient id="damask-tone" cx="0.3" cy="0.55" r="0.8">
        <stop offset="0" stop-color="#262626"/>
        <stop offset="1" stop-color="#0a0a0a"/>
      </radialGradient>
      <linearGradient id="panel-tone" gradientUnits="userSpaceOnUse" x1="0" y1="0" x2="0" y2="2250">
        <stop offset="0" stop-color="#151515"/>
        <stop offset="0.28" stop-color="#1b1b1b"/>
        <stop offset="0.42" stop-color="#555555"/>
        <stop offset="0.65" stop-color="#7c7c7c"/>
        <stop offset="1" stop-color="#3c3c3c"/>
      </linearGradient>
      <linearGradient id="ribbon-tone" x1="0" y1="0" x2="1" y2="0">
        <stop offset="0" stop-color="var(--silver-dark)"/>
        <stop offset="0.5" stop-color="var(--silver-light)"/>
        <stop offset="1" stop-color="var(--silver-mid)"/>
      </linearGradient>
    </defs>

    <rect class="damask-field" width="1200" height="2877" fill="url(#damask-tone)"
          role="img" aria-label="Zwart damastpatroon als achtergrond"/>

    <path class="header-and-portrait" fill="url(#panel-tone)"
          role="img" aria-label="Donker paneel met daaronder een zwart-witfoto van een vrouw met opgestoken haar"
          d="M340 0 C220 300 200 700 420 1100 C600 1450 900 1800 1200 2180 L1200 0 Z"/>

    <path class="silver-ribbon" fill="url(#ribbon-tone)"
          d="M318 0 C195 300 175 700 392 1112 C572 1475 870 1850 1200 2290
             L1200 2180 C900 1800 600 1450 420 1100 C200 700 220 300 340 0 Z"/>
    <path class="ribbon-edge" fill="none" stroke="var(--silver-light)" stroke-width="4" opacity="0.85"
          d="M340 0 C220 300 200 700 420 1100 C600 1450 900 1800 1200 2180"/>
  </svg>

  <h1 class="brand">VELMORA</h1>

  <ul class="services">
    <li>Gelaatsverzorging</li>
    <li>Wimperverlenging</li>
    <li>Wimperlifting</li>
    <li>Suikerontharing</li>
    <li>Permanente Make Up</li>
    <li>Airbrush Tanning</li>
    <li>Manicure - Pedicure - Tovira</li>
  </ul>

  <div class="contact">
    <p class="web">www.velmora.be</p>
    <p class="call">Enkel op afspraak,<br>bel 0486319542</p>
  </div>
</main>
</body>
</html>
```